New website design for tech company

I want to redesign the current website - https://quorvalent.co/
I want it to keep the same colors/branding but I want it to resemble the look and feel of the following sites
https://www.drelkusa.com/
https://www.munoro.com/
https://www.pulvane.com/global/us/home
https://www.tovinplc.co.uk/

The site layout

Target Market(s)

tech companies

Industry/Entity Type

tech

Number of Pages Required

2 page

Font styles to use
Serif

Colors

Designer to choose colors to be used in the design.

Requirements
Must have
• a nice updated design that looks cutting edge and innovative and the site colors can match the current logo

```html
<!DOCTYPE html>
<html lang="en">
<head>
<meta charset="utf-8">
<title>Quorvalent – Transform Your Business with Technology</title>
<link href="https://fonts.googleapis.com/css2?family=Montserrat:wght@400;500;600;700;800&family=Urbanist:wght@400;500;600;700&display=swap" rel="stylesheet">
<style>
:root{
  --blue:#0b57c8;
  --blue-dark:#0a4aa8;
  --green:#8cc63f;
  --ink:#111418;
  --text:#3a3f47;
  --muted:#6b7280;
  --soft:#eaf0f8;
  --line:#d6dbe3;
  --white:#ffffff;
}
*{margin:0;padding:0;box-sizing:border-box}
html,body{width:1200px;height:3387px;overflow:hidden}
body{font-family:"Urbanist",sans-serif;color:var(--text);background:var(--white);position:relative}
.wrap{width:918px;margin:0 auto;position:relative}
h2.section-title{font-family:"Montserrat",sans-serif;font-weight:400;font-size:32px;color:var(--ink);text-align:center;letter-spacing:.3px}
h2.section-title b{font-weight:700}

/* header */
.site-header{height:68px;display:flex;align-items:center}
.site-header .wrap{display:flex;align-items:center;justify-content:space-between}
.brand{display:flex;align-items:center;gap:8px;font-family:"Montserrat",sans-serif;font-weight:800;font-size:22px;color:var(--green);letter-spacing:1px}
.brand-dot{width:16px;height:16px;border-radius:50%;background:var(--blue)}
.main-nav{display:flex;align-items:center;gap:34px;font-size:13px;color:var(--ink);font-weight:500}
.btn{display:inline-flex;align-items:center;justify-content:center;border-radius:30px;color:var(--white);font-size:12.5px;font-weight:600;text-transform:uppercase;letter-spacing:.3px}
.btn-blue{background:var(--blue)}
.btn-green{background:var(--green)}
.main-nav .btn{width:120px;height:40px}

/* hero */
.hero{position:relative;height:459px;overflow:hidden}
.hero-bg{position:absolute;inset:0;background:linear-gradient(90deg,#1b2231 0%,#2b3444 40%,#4a5668 65%,#2a3344 100%)}
.hero-content{position:relative;padding-top:112px;color:var(--white)}
.hero-kicker{font-size:17px;font-weight:500}
.hero h1{font-family:"Montserrat",sans-serif;font-weight:800;font-size:37px;line-height:42px;margin-top:18px}
.hero-sub{font-size:23px;line-height:31px;margin-top:12px;font-weight:500}
.hero .btn{width:140px;height:38px;margin-top:20px;font-weight:500}

/* about */
.about{height:588px}
.about .wrap{display:flex;padding-top:85px}
.about-photo{width:412px;height:413px;position:relative;flex:none}
.about-photo .frame{position:absolute;left:8px;top:0;right:0;bottom:0;border:2px solid var(--blue);border-radius:0 14px 14px 14px}
.about-photo .img{position:absolute;left:0;top:0;width:406px;height:405px;border-radius:12px;background:linear-gradient(160deg,#c9ccd1,#7f858d 55%,#3c4048)}
.about-text{margin-left:107px;width:400px}
.about-text h2{font-family:"Montserrat",sans-serif;font-weight:400;font-size:31px;color:var(--ink)}
.about-text h2 b{font-weight:700}
.about-text h3{font-size:20px;font-weight:400;color:var(--ink);letter-spacing:.4px;margin:6px 0 16px}
.about-text h3 b{font-weight:600}
.about-text p{font-size:13px;line-height:22px;margin-bottom:11px}
.about-text .btn{width:141px;height:38px;margin-top:14px}

/* services */
.services{height:563px;background:var(--soft);padding-top:78px}
.services .intro{width:840px;margin:12px auto 0;text-align:center;font-size:13px;line-height:18.5px;color:var(--ink)}
.service-grid{display:flex;gap:25px;margin:24px 0 0 10px}
.service-card{width:283px;height:282px;background:var(--white);border-radius:8px;box-shadow:0 2px 10px rgba(20,40,80,.08);padding:16px 0 0 28px;position:relative}
.service-card .icon{width:54px;height:54px}
.service-card .rule{position:relative;height:1px;background:var(--line);margin-top:20px}
.service-card .rule::before{content:"";position:absolute;left:0;top:-5px;width:10px;height:10px;border:1.5px solid var(--green);border-radius:50%;background:var(--white)}
.service-card h3{font-size:18px;font-weight:600;color:var(--ink);margin-top:30px}
.service-card p{font-size:11.5px;line-height:19px;margin-top:10px;width:222px}
.service-card a{display:block;margin-top:12px;font-size:11px;font-weight:700;color:var(--blue);text-decoration:underline}

/* partners */
.partners{height:425px;padding-top:73px;position:relative}
.partner-row{display:flex;gap:16px;margin-top:21px}
.partner{width:171px;height:109px;border:1px solid var(--line);border-bottom:2px solid var(--blue);display:flex;align-items:center;justify-content:center}
.partner span{width:90px;height:26px;border-radius:4px;background:#dfe6f1}
.arrow{position:absolute;width:36px;height:36px;border-radius:50%;display:flex;align-items:center;justify-content:center}
.arrow.prev{background:var(--white);box-shadow:0 2px 8px rgba(0,0,0,.12)}
.arrow.next{background:var(--blue)}
.partners .arrow{top:193px}
.partners .prev{left:83px}.partners .next{left:1079px}

/* testimonials */
.testimonials{height:496px;position:relative}
.testimonial-row{display:flex;gap:35px;margin-top:18px;padding-left:1px}
.testimonial{width:283px;text-align:center}
.bubble{position:relative;height:162px;background:var(--white);border-radius:12px;box-shadow:0 3px 14px rgba(20,40,80,.1);padding:36px 12px 0;font-size:10.6px;line-height:19px;color:var(--text)}
.bubble::after{content:"";position:absolute;left:50%;bottom:-14px;margin-left:-14px;border-left:14px solid transparent;border-right:14px solid transparent;border-top:14px solid var(--white)}
.avatar{width:58px;height:58px;border-radius:50%;border:2px solid var(--blue);margin:45px auto 0;background:linear-gradient(#c7ccd4,#8c939e)}
.testimonial h4{font-family:"Montserrat",sans-serif;font-size:13.5px;font-weight:700;color:var(--ink);margin-top:16px}
.testimonial small{font-size:11px;color:var(--muted)}
.testimonials .arrow{top:270px}
.testimonials .prev{left:83px}.testimonials .next{left:1079px}

/* contact */
.contact{height:519px;padding-top:10px}
.contact-grid{display:flex;justify-content:space-between;margin-top:20px}
.contact-left{width:432px;padding-left:22px}
.map{width:414px;height:204px;border-radius:4px;background:linear-gradient(135deg,#e4ebf1,#c9d8e6 60%,#dfe7ee)}
.contact-left h3{font-family:"Montserrat",sans-serif;font-size:21px;font-weight:500;color:var(--ink);margin:45px 0 0 7px;letter-spacing:.4px}
.contact-left h3 b{font-weight:700}
.detail{display:flex;align-items:center;gap:16px;font-size:12.5px;line-height:20px;color:var(--ink)}
.detail .ic{width:30px;height:30px;border-radius:50%;box-shadow:0 1px 6px rgba(0,0,0,.15);display:flex;align-items:center;justify-content:center;flex:none}
.detail-row{display:flex;gap:44px;margin:20px 0 0 6px}
.contact-form{width:412px}
.field{border:1px solid var(--line);height:50px;display:flex;align-items:center;padding-left:12px;gap:16px;font-size:12.5px;color:var(--text);margin-bottom:10px}
.field.message{height:99px;align-items:flex-start;padding-top:14px}
.form-links{text-align:center;font-size:12px;margin-top:12px;color:var(--text)}
.check{display:flex;align-items:center;justify-content:center;gap:8px;font-size:12px;color:var(--ink);margin-top:9px}
.check i{width:16px;height:16px;border:1px solid #b7bec8}
.check em{color:#d33;font-style:normal}
.contact-form .btn{display:flex;width:99px;height:38px;margin:16px auto 0}

/* footer */
.site-footer{position:absolute;left:0;right:0;top:3128px;bottom:0;background:var(--blue);color:var(--white);text-align:center}
.site-footer .brand{justify-content:center;color:var(--white);font-size:32px;margin-top:50px}
.site-footer .brand-dot{background:var(--white);width:22px;height:22px}
.tagline{font-size:13px;margin-top:24px}
.foot-nav{border-top:1px solid rgba(255,255,255,.35);border-bottom:1px solid rgba(255,255,255,.35);height:55px;display:flex;align-items:center;justify-content:center;gap:34px;font-size:13px;margin-top:24px}
.foot-bottom{display:flex;justify-content:space-between;align-items:center;height:40px;font-size:12px}
.social{display:flex;gap:22px}
.social span{width:9px;height:9px;background:var(--white);border-radius:2px}
</style>
</head>
<body>

<header class="site-header">
  <div class="wrap">
    <div class="brand"><span class="brand-dot"></span>QUORVALENT</div>
    <nav class="main-nav">
      <span>Home</span><span>About</span><span>Media</span><span>Services</span><span>Blog</span>
      <span class="btn btn-blue">Contact</span>
    </nav>
  </div>
</header>

<section class="hero">
  <div class="hero-bg" role="img" aria-label="Businessman in a suit working on a laptop with glowing globe and code overlays"></div>
  <div class="wrap hero-content">
    <p class="hero-kicker">Quorvalent - A subsidiary of Marlowe &amp; Co.</p>
    <h1>Transform Your Business<br>with Technology</h1>
    <p class="hero-sub">Expertise in Web Development, Cybersecurity,<br>and Cloud Computing</p>
    <span class="btn btn-green">Ask us now</span>
  </div>
</section>

<section class="about">
  <div class="wrap">
    <div class="about-photo">
      <div class="frame"></div>
      <div class="img" role="img" aria-label="Team of business professionals walking down office stairs"></div>
    </div>
    <div class="about-text">
      <h2>ABOUT <b>US</b></h2>
      <h3>What is <b>Quorvalent?</b></h3>
      <p>Quorvalent is a web based Internet and technology agency aimed at serving, educating, and partnering with brands &amp; organizations on how their products and services can advance the disabled community through inclusion and diversity.</p>
      <p>By integrating strategies, solutions, and practices accommodating all persons, we strive to shift humanity forward with the power of technology.</p>
      <h3 style="margin-top:14px">Our <b>Mission</b></h3>
      <p>To increase awareness and opportunities in the personal &amp; professional lives of disabled persons through technology, regardless of gender, age race or socio-economic background.</p>
      <span class="btn btn-blue">Know more</span>
    </div>
  </div>
</section>

<section class="services">
  <h2 class="section-title">OUR <b>SERVICES</b></h2>
  <p class="intro">Quorvalent is a web based Internet and technology agency aimed at serving, educating, and partnering with brands &amp; organizations on how their products and services can advance the disabled community through inclusion and diversity. By integrating strategies, solutions, and practices accommodating all persons, we strive to shift humanity forward with the power of technology.</p>
  <div class="wrap">
    <div class="service-grid">
      <article class="service-card">
        <svg class="icon" viewBox="0 0 54 54" fill="none" stroke-width="2"><rect x="3" y="4" width="46" height="46" rx="4" stroke="#0b57c8"/><line x1="3" y1="14" x2="49" y2="14" stroke="#0b57c8"/><circle cx="9" cy="9" r="1.5" fill="#8cc63f" stroke="none"/><circle cx="14" cy="9" r="1.5" fill="#8cc63f" stroke="none"/><path d="M18 26l-6 6 6 6M36 26l6 6-6 6M30 23l-6 18" stroke="#8cc63f"/></svg>
        <div class="rule"></div>
        <h3>Web Development</h3>
        <p>Lorem Ipsum ist einfach der Blindtext der Druck- und Setzindustrie. Lorem Ipsum ist der Standard-Blindtext der Branche seit dem Jahr 1500, als ein....</p>
        <a>KNOW MORE</a>
      </article>
      <article class="service-card">
        <svg class="icon" viewBox="0 0 54 54" fill="none" stroke-width="2"><rect x="3" y="6" width="48" height="32" rx="3" stroke="#0b57c8"/><path d="M20 38v8h14v-8M14 47h26" stroke="#0b57c8"/><rect x="30" y="16" width="14" height="12" rx="2" stroke="#8cc63f"/><path d="M33 16v-4a4 4 0 018 0v4" stroke="#8cc63f"/><path d="M9 14h10M9 20h6M9 26h12" stroke="#0b57c8"/></svg>
        <div class="rule"></div>
        <h3>Cybersecurity</h3>
        <p>Lorem Ipsum ist einfach der Blindtext der Druck- und Setzindustrie. Lorem Ipsum ist der Standard-Blindtext der Branche seit dem Jahr 1500, als ein....</p>
        <a>KNOW MORE</a>
      </article>
      <article class="service-card">
        <svg class="icon" viewBox="0 0 64 54" fill="none" stroke-width="2"><path d="M16 36h-4a9 9 0 010-18 14 14 0 0127-3 10 10 0 0113 10 8 8 0 01-2 11h-8" stroke="#8cc63f"/><rect x="18" y="26" width="20" height="14" rx="2" stroke="#0b57c8"/><path d="M25 40v5h6v-5M22 46h12" stroke="#0b57c8"/></svg>
        <div class="rule"></div>
        <h3>Cloud Computing</h3>
        <p>Lorem Ipsum ist einfach der Blindtext der Druck- und Setzindustrie. Lorem Ipsum ist der Standard-Blindtext der Branche seit dem Jahr 1500, als ein....</p>
        <a>KNOW MORE</a>
      </article>
    </div>
  </div>
</section>

<section class="partners">
  <h2 class="section-title">OUR <b>TECHNOLOGY PARTNERS</b></h2>
  <div class="wrap">
    <div class="partner-row">
      <div class="partner"><span></span></div>
      <div class="partner"><span></span></div>
      <div class="partner"><span></span></div>
      <div class="partner"><span></span></div>
      <div class="partner"><span></span></div>
    </div>
  </div>
  <span class="arrow prev"><svg width="12" height="12" viewBox="0 0 12 12"><path d="M8 1L3 6l5 5" stroke="#0b57c8" stroke-width="2" fill="none"/></svg></span>
  <span class="arrow next"><svg width="12" height="12" viewBox="0 0 12 12"><path d="M4 1l5 5-5 5" stroke="#fff" stroke-width="2" fill="none"/></svg></span>
</section>

<section class="testimonials">
  <h2 class="section-title">CLIENT <b>TESTIMONIALS</b></h2>
  <div class="wrap">
    <div class="testimonial-row">
      <div class="testimonial">
        <div class="bubble">Lorem Ipsum ist einfach der Blindtext der Druck- und Setzindustrie. Lorem Ipsum ist der Standard-Blindtext der Branche seit dem Jahr 1500, als ein unbekannter Drucker eine Druckfahne nahm und sie zu ein</div>
        <div class="avatar" role="img" aria-label="Client portrait"></div>
        <h4>Harlan P.</h4><small>Quorvalent</small>
      </div>
      <div class="testimonial">
        <div class="bubble">Lorem Ipsum ist einfach der Blindtext der Druck- und Setzindustrie. Lorem Ipsum ist der Standard-Blindtext der Branche seit dem Jahr 1500, als ein unbekannter Drucker eine Druckfahne nahm und sie zu ein</div>
        <div class="avatar" role="img" aria-label="Client portrait"></div>
        <h4>Selene M.</h4><small>Quorvalent</small>
      </div>
      <div class="testimonial">
        <div class="bubble">Lorem Ipsum ist einfach der Blindtext der Druck- und Setzindustrie. Lorem Ipsum ist der Standard-Blindtext der Branche seit dem Jahr 1500, als ein unbekannter Drucker eine Druckfahne nahm und sie zu ein</div>
        <div class="avatar" role="img" aria-label="Client portrait"></div>
        <h4>Tobias R.</h4><small>Quorvalent</small>
      </div>
    </div>
  </div>
  <span class="arrow prev"><svg width="12" height="12" viewBox="0 0 12 12"><path d="M8 1L3 6l5 5" stroke="#0b57c8" stroke-width="2" fill="none"/></svg></span>
  <span class="arrow next"><svg width="12" height="12" viewBox="0 0 12 12"><path d="M4 1l5 5-5 5" stroke="#fff" stroke-width="2" fill="none"/></svg></span>
</section>

<section class="contact">
  <h2 class="section-title">CONTACT <b>US</b></h2>
  <div class="wrap">
    <div class="contact-grid">
      <div class="contact-left">
        <div class="map" role="img" aria-label="Street map of the office area with a location pin"></div>
        <h3>CONTACT <b>DETAILS</b></h3>
        <div class="detail" style="margin:22px 0 0 6px">
          <span class="ic"><svg width="12" height="14" viewBox="0 0 12 14"><path d="M6 13s5-5 5-8a5 5 0 00-10 0c0 3 5 8 5 8z" fill="none" stroke="#0b57c8" stroke-width="1.6"/><circle cx="6" cy="5" r="1.6" fill="#0b57c8"/></svg></span>
          <span>Quorvalent Halden Bay, Westmere<br>(555) QUORVA - 9</span>
        </div>
        <div class="detail-row">
          <div class="detail">
            <span class="ic"><svg width="14" height="12" viewBox="0 0 14 12"><rect x="1" y="1" width="12" height="10" rx="1" fill="none" stroke="#0b57c8" stroke-width="1.5"/><path d="M1 2l6 5 6-5" fill="none" stroke="#0b57c8" stroke-width="1.5"/></svg></span>
            <span>Email<br>hello@quorvalent.co</span>
          </div>
          <div class="detail">
            <span class="ic"><svg width="14" height="14" viewBox="0 0 14 14"><path d="M3 1l3 3-2 2a8 8 0 004 4l2-2 3 3-2 2C6 13 1 8 1 3z" fill="#0b57c8"/></svg></span>
            <span>Phone<br>555-014-2290</span>
          </div>
        </div>
      </div>
      <form class="contact-form">
        <div class="field"><svg width="12" height="13" viewBox="0 0 12 13"><circle cx="6" cy="3.5" r="3" fill="#0b57c8"/><path d="M0 13a6 6 0 0112 0z" fill="#0b57c8"/></svg>Name*</div>
        <div class="field"><svg width="14" height="11" viewBox="0 0 14 11"><rect width="14" height="11" rx="1.5" fill="#0b57c8"/><path d="M1 1l6 5 6-5" fill="none" stroke="#fff" stroke-width="1.3"/></svg>Email*</div>
        <div class="field"><svg width="13" height="13" viewBox="0 0 14 14"><path d="M3 1l3 3-2 2a8 8 0 004 4l2-2 3 3-2 2C6 13 1 8 1 3z" fill="#0b57c8"/></svg>Phone*</div>
        <div class="field message"><svg width="15" height="13" viewBox="0 0 15 13"><path d="M1 1h9v6H5l-3 2V7H1z" fill="#0b57c8"/><path d="M11 4h3v6h-1v2l-3-2H6V8h5z" fill="#0b57c8"/></svg>Message</div>
        <p class="form-links">Disclaimer &nbsp; | &nbsp; Privacy Policy</p>
        <div class="check"><i></i>I Have Read The Disclaimer<em>*</em></div>
        <span class="btn btn-blue">Submit</span>
      </form>
    </div>
  </div>
</section>

<footer class="site-footer">
  <div class="brand"><span class="brand-dot"></span>QUORVALENT</div>
  <p class="tagline">Without a vision the people will perish. Pr 29.11</p>
  <div class="wrap">
    <nav class="foot-nav"><span>Home</span><span>About</span><span>Media</span><span>Services</span><span>Blog</span><span>Contact</span></nav>
    <div class="foot-bottom">
      <span>Copyright © 2024 Quorvalent - All Rights Reserved</span>
      <span class="social"><span></span><span></span><span></span><span></span></span>
    </div>
  </div>
</footer>

</body>
</html>
```